Dog treat bakery needs updated bag labels

We're a small-batch dog treat bakery and would like to update our front bag labels to 1) differentiate our line of products and 2) to stand out on shelves. We believe all dogs deserve to eat clean, healthy foods. That's why we bake low-calorie, clean treats made with simple, premium ingredients like teff, amaranth, and sorghum flours and 100% blueberry, carrot, and purple sweet potato. All our treats are made gluten free without preservatives, artificial flavors, soy, corn, wheat, or eggs. Clean treats, happy dogs!

see uploaded files

```html
<!DOCTYPE html>
<html lang="en">
<head>
<meta charset="utf-8">
<title>Perky Pup – bag label</title>
<link href="https://fonts.googleapis.com/css2?family=Patua+One&family=PT+Sans&display=swap" rel="stylesheet">
<style>
  :root {
    --page-light: #ffffff;
    --page-dark: #000000;
    --label-fill: #e6e7e8;
    --accent-orange: #f15a29;
    --accent-blue: #27aae1;
    --ink: #231f20;
    --art-tone: #f4f4f4;
  }
  html, body {
    margin: 0;
    padding: 0;
    width: 1200px;
    height: 1117px;
    overflow: hidden;
  }
  .canvas { display: block; width: 1200px; height: 1117px; }
  .stage-light { fill: var(--page-light); }
  .stage-dark { fill: var(--page-dark); }
  .label-shape { fill: var(--label-fill); stroke: var(--accent-orange); stroke-width: 1; }
  .tagline-main, .tagline-sub, .brand-name {
    font-family: "Patua One", Georgia, serif;
    fill: var(--accent-orange);
  }
  .tagline-main { font-size: 44px; letter-spacing: 1px; }
  .tagline-sub { font-size: 29px; letter-spacing: 1px; }
  .brand-name { font-size: 50px; letter-spacing: 3px; }
  .ingredients-title {
    font-family: "PT Sans", Arial, sans-serif;
    font-size: 19px;
    fill: var(--accent-blue);
  }
  .ingredients-copy {
    font-family: "PT Sans", Arial, sans-serif;
    font-size: 13.5px;
    fill: var(--ink);
  }
  .mascot-art { fill: var(--art-tone); }
</style>
</head>
<body>
<svg class="canvas" viewBox="0 0 1200 1117" xmlns="http://www.w3.org/2000/svg">
  <rect class="stage-light" x="0" y="0" width="1200" height="603"/>
  <rect class="stage-dark" x="0" y="603" width="1200" height="514"/>

  <!-- Label on light stage -->
  <g class="bag-label">
    <path class="label-shape" d="M81 218 H415 A190 190 0 0 1 755 218 H1139 V387 H755 A190 190 0 0 1 415 387 H81 Z"/>
    <text class="tagline-main" x="110" y="290">happy dogs</text>
    <text class="tagline-sub" x="142" y="331">Clean treats</text>
    <text class="brand-name" x="585" y="205" text-anchor="middle">Perky Pup</text>
    <circle class="mascot-art" cx="585" cy="335" r="100" role="img" aria-label="Illustration of a smiling dog mascot wearing an orange bandana"/>
    <text class="ingredients-title" x="928" y="257" text-anchor="middle">premium ingredients</text>
    <text class="ingredients-copy" text-anchor="middle">
      <tspan x="928" y="275">like teff, amaranth, and sorghum flours</tspan>
      <tspan x="928" y="292">and %100 blueberry, carrot,</tspan>
      <tspan x="928" y="310">and purple sweet potato.</tspan>
      <tspan x="928" y="327">All our treats are made gluten free</tspan>
      <tspan x="928" y="344">without preservatives,</tspan>
      <tspan x="928" y="362">artificial flavors, soy, corn, wheat, or eggs.</tspan>
    </text>
  </g>

  <!-- Label on dark stage -->
  <g class="bag-label" transform="translate(0 540)">
    <path class="label-shape" d="M81 218 H415 A190 190 0 0 1 755 218 H1139 V387 H755 A190 190 0 0 1 415 387 H81 Z"/>
    <text class="tagline-main" x="110" y="290">happy dogs</text>
    <text class="tagline-sub" x="142" y="331">Clean treats</text>
    <text class="brand-name" x="585" y="205" text-anchor="middle">Perky Pup</text>
    <circle class="mascot-art" cx="585" cy="335" r="100" role="img" aria-label="Illustration of a smiling dog mascot wearing an orange bandana"/>
    <text class="ingredients-title" x="928" y="257" text-anchor="middle">premium ingredients</text>
    <text class="ingredients-copy" text-anchor="middle">
      <tspan x="928" y="275">like teff, amaranth, and sorghum flours</tspan>
      <tspan x="928" y="292">and %100 blueberry, carrot,</tspan>
      <tspan x="928" y="310">and purple sweet potato.</tspan>
      <tspan x="928" y="327">All our treats are made gluten free</tspan>
      <tspan x="928" y="344">without preservatives,</tspan>
      <tspan x="928" y="362">artificial flavors, soy, corn, wheat, or eggs.</tspan>
    </text>
  </g>
</svg>
</body>
</html>
```